Do i have coronavirus, flue or cold?

Using information from PFA and government agencies we want to make a easy to read infographic helping patients see if they have coronavirus, the flu or a cold. Using a flow diagram or whatever you think will make it easy to read and digest for the average lamen.

Information is in the word document and in the chart.

We are www.calvexa.co.uk attached is our brand guidelines, we will be putting this infographic on our website and email/sms it to all of our 300,000 patients.

```html
<!DOCTYPE html>
<html lang="en">
<head>
<meta charset="utf-8">
<title>Do I have coronavirus, flu or cold?</title>
<link rel="stylesheet" href="https://fonts.googleapis.com/css2?family=Poppins:wght@400;500;700&display=swap">
<style>
  :root {
    --page-bg: #13132f;
    --header-bg: #4348a0;
    --ink-blue: #3f47a0;
    --corona-bg: #edf4f5;
    --flu-bg: #7889c6;
    --cold-bg: #f4a283;
    --tag-red: #e52b2b;
    --text-dark: #3a3a3a;
    --white: #ffffff;
    --leader-orange: #f06a35;
    --leader-blue: #3a5fd0;
  }
  * { box-sizing: border-box; margin: 0; padding: 0; }
  html, body { width: 1200px; height: 1200px; overflow: hidden; }
  body {
    background: var(--page-bg);
    font-family: "Poppins", sans-serif;
    position: relative;
  }
  .infographic {
    position: absolute;
    left: 280px;
    top: 24px;
    width: 640px;
    height: 1152px;
  }
  .masthead {
    height: 111px;
    background: var(--header-bg);
    color: var(--white);
    display: flex;
    align-items: center;
    justify-content: center;
    text-align: center;
    font-weight: 700;
    font-size: 34px;
    line-height: 39px;
    letter-spacing: 1.5px;
  }
  .condition {
    position: relative;
    height: 347px;
    overflow: hidden;
  }
  .condition--corona { background: var(--corona-bg); }
  .condition--flu { background: var(--flu-bg); }
  .condition--cold { background: var(--cold-bg); }
  .condition__diagram {
    position: absolute;
    inset: 0;
    width: 100%;
    height: 100%;
  }
  .condition__title {
    position: absolute;
    top: 50px;
    font-weight: 700;
    font-size: 40px;
    line-height: 1;
    color: var(--ink-blue);
  }
  .condition--flu .condition__title { color: var(--white); right: 49px; }
  .condition--corona .condition__title,
  .condition--cold .condition__title { left: 37px; }
  .symptom-tag {
    position: absolute;
    top: 140px;
    background: var(--tag-red);
    color: var(--white);
    font-weight: 500;
    font-size: 13px;
    line-height: 17px;
    padding: 0 11px;
    letter-spacing: 0.4px;
  }
  .condition--corona .symptom-tag,
  .condition--cold .symptom-tag { left: 37px; }
  .condition--flu .symptom-tag { right: 52px; }
  .condition__summary {
    position: absolute;
    top: 180px;
    font-size: 20px;
    line-height: 23px;
    letter-spacing: 0.3px;
  }
  .condition--corona .condition__summary { left: 37px; width: 230px; color: var(--text-dark); }
  .condition--flu .condition__summary { right: 49px; width: 220px; text-align: right; color: var(--white); }
  .condition--cold .condition__summary { left: 38px; width: 200px; font-size: 20px; color: var(--white); }
  .label { font-family: "Poppins", sans-serif; font-size: 12px; letter-spacing: 0.3px; }
  .label--dark { fill: var(--text-dark); }
  .label--light { fill: var(--white); }
  .leader { fill: none; stroke-width: 1.2; }
  .leader--orange { stroke: var(--leader-orange); }
  .leader--white { stroke: var(--white); }
  .leader--blue { stroke: var(--leader-blue); }
</style>
</head>
<body>
<main class="infographic">
  <header class="masthead"><h1 style="font:inherit">DO I HAVE CORONAVIRUS,<br>FLU OR COLD?</h1></header>

  <section class="condition condition--corona">
    <svg class="condition__diagram" viewBox="0 0 894 485" preserveAspectRatio="none">
      <defs>
        <radialGradient id="coronaFill" cx="50%" cy="45%" r="60%">
          <stop offset="0" stop-color="#5a5fb4"/>
          <stop offset="1" stop-color="#ffffff"/>
        </radialGradient>
      </defs>
      <circle role="img" aria-label="Illustration of a woman in a face mask and orange scarf coughing" cx="628" cy="265" r="150" fill="url(#coronaFill)"/>
      <path class="leader leader--orange" d="M486 113H578L588 120"/>
      <text class="label label--dark" x="490" y="128">FEVER</text>
      <path class="leader leader--orange" d="M798 100H711L673 127"/>
      <text class="label label--dark" x="738" y="114">TIREDNESS</text>
      <path class="leader leader--orange" d="M416 180H516L543 195"/>
      <text class="label label--dark" x="419" y="195">DRY COUGH</text>
      <path class="leader leader--orange" d="M843 180H753L736 192"/>
      <text class="label label--dark" x="759" y="195">MUSCLE ACHES</text>
      <text class="label label--dark" x="397" y="264">SHORTNESS</text>
      <text class="label label--dark" x="400" y="278">OF BREATH</text>
      <path class="leader leader--orange" d="M390 282H490L518 262"/>
      <path class="leader leader--orange" d="M858 305H761L693 277"/>
      <text class="label label--dark" x="775" y="300">SORE THROAT</text>
    </svg>
    <h2 class="condition__title">CORONAVIRUS</h2>
    <span class="symptom-tag">SYMTOMS</span>
    <p class="condition__summary">These symptoms are usually mild and begin gradually.</p>
  </section>

  <section class="condition condition--flu">
    <svg class="condition__diagram" viewBox="0 0 894 485" preserveAspectRatio="none">
      <defs>
        <radialGradient id="fluFill" cx="50%" cy="45%" r="60%">
          <stop offset="0" stop-color="#4348a0"/>
          <stop offset="1" stop-color="#f2f4fa"/>
        </radialGradient>
      </defs>
      <circle role="img" aria-label="Illustration of a man with a thermometer, holding his chest" cx="298" cy="276" r="145" fill="url(#fluFill)"/>
      <path class="leader leader--white" d="M126 112H223L243 123"/>
      <text class="label label--light" x="130" y="126">HIGH FEVER</text>
      <path class="leader leader--white" d="M433 95H343L323 109"/>
      <text class="label label--light" x="371" y="109">HEADACHE</text>
      <path class="leader leader--white" d="M78 194H161L178 206"/>
      <text class="label label--light" x="81" y="209">COUGH</text>
      <text class="label label--light" x="55" y="296">SHORTNESS</text>
      <text class="label label--light" x="58" y="311">OF BREATH</text>
      <path class="leader leader--white" d="M53 318H153L200 296"/>
      <path class="leader leader--white" d="M513 194H418L403 181"/>
      <text class="label label--light" x="418" y="188">MUSCLE ACHES</text>
      <path class="leader leader--white" d="M523 261H453L438 249"/>
      <text class="label label--light" x="456" y="255">TIREDNESS</text>
    </svg>
    <h2 class="condition__title">FLU</h2>
    <span class="symptom-tag">SYMTOMS</span>
    <p class="condition__summary">Flu symptoms often come on suddenly,</p>
  </section>

  <section class="condition condition--cold">
    <svg class="condition__diagram" viewBox="0 0 894 485" preserveAspectRatio="none">
      <defs>
        <radialGradient id="coldFill" cx="50%" cy="45%" r="60%">
          <stop offset="0" stop-color="#4348a0"/>
          <stop offset="1" stop-color="#edf4f5"/>
        </radialGradient>
      </defs>
      <circle role="img" aria-label="Illustration of a woman in a scarf sneezing and holding a hot drink" cx="598" cy="250" r="165" fill="url(#coldFill)"/>
      <path class="leader leader--blue" d="M358 125H456L488 145"/>
      <text class="label label--dark" x="363" y="140">SNEEZING</text>
      <path class="leader leader--blue" d="M336 187H436L465 204"/>
      <text class="label label--dark" x="339" y="199">RUNY NOSE</text>
      <path class="leader leader--blue" d="M326 278H423L450 255"/>
      <text class="label label--dark" x="328" y="270">LOSE OF TASTE</text>
      <path class="leader leader--blue" d="M823 122H706L668 149"/>
      <text class="label label--dark" x="712" y="137">MODERATE COUGHS</text>
      <text class="label label--dark" x="769" y="242">MILD</text>
      <text class="label label--dark" x="738" y="256">MUSCLE ACHES</text>
      <path class="leader leader--blue" d="M833 259H738L698 245"/>
    </svg>
    <h2 class="condition__title">COLD</h2>
    <span class="symptom-tag">SYMTOMS</span>
    <p class="condition__summary">Sneezing, runny and Stuffy Nose, are most common symptoms of Cold.</p>
  </section>
</main>
</body>
</html>
```